New Phone Case requires logo and packaging

We need a nice and sleek logo designed along with packaging for our Premium Phone Case brand

Our Brand Name is Vaxel
Please note this has nothing to do with a Rhino so don't put a Rhino in the logo
I've also attached a file called VAXEL Logo Inspiration, which shows something along the lines of the type of text we want to use. Please note i have photoshopped that image together from another logo we had, and i liked the text, but its for you to see what direction we want to go in. Also note i have shown different variations in that image file, use your imagination with it and show us a nice and clean logo.

We would like the Brand in upper caps such as VAXEL
The brand is for Premium Phone Cases. The first thing that should come to someones mind when looking at the branding is High Quality, Premium and Modern.

The look must be high end and modern

The design must portray high quality and premium!

Also i will say "Less is More". Don't cramp many things on the packaging and logo. We just want a nice, clean cut high quality logo and packaging

I have attached images of an example packaging from a few competitors. One is a standard open from top packaging, while another is a slide out packaging. Our packaging dimensions should be the same which are Packaging dimensions
Length = 18cm
Height = 1.5cm
Depth = 9.5cm

Also note the example packaging has a transparent front section to show which case is inside, this is optional if you want to have it. If not you can cover it all up.

Font styles to use
Other font styles liked:
• Any nice font but just not the standard everyday stuff like Arial, San Serif etc as i want it to be differentiated. A Font that shows Serious Quality and one that stands out would be awesome!

Colors

Designer to choose colors to be used in the design.

Requirements
Must have
• Must be a nice and clean design
• Packaging dimensions
• Length = 18cm
• Height = 1.5cm
• Depth = 9.5cm

```html
<!DOCTYPE html>
<html lang="en">
<head>
<meta charset="utf-8">
<title>Vaxel Packaging</title>
<link href="https://fonts.googleapis.com/css2?family=Jost:wght@300;400;500;600&display=swap" rel="stylesheet">
<style>
  :root{
    --bg:#ffffff;
    --sleeve:#131110;
    --tray:#0b0b0c;
    --tab:#c8201f;
    --gold:#c9a86a;
    --paper:#ffffff;
    --ink:#1c1c1c;
    --copy:#ffffff;
  }
  *{margin:0;padding:0;box-sizing:border-box}
  html,body{width:1200px;height:1200px;overflow:hidden;background:var(--bg);font-family:'Jost',sans-serif}
  .canvas{position:relative;width:1200px;height:1200px}
  .abs{position:absolute}
  .tab{background:var(--tab);border-radius:16px 16px 0 0}
  .tab--thin{border-radius:5px 5px 0 0}
  .tray{background:var(--tray)}
  .tray--front{border:7px solid #201c1c;border-bottom:none}
  .case-photo{position:absolute;left:23px;top:17px;width:308px;height:107px;border-radius:24px 24px 0 0;background:linear-gradient(180deg,#f7f7f7,#e6e6e6)}
  .sleeve{background:var(--sleeve)}
  .sleeve-foot{background:var(--paper)}
  .wordmark{color:var(--gold);font-weight:500;letter-spacing:.04em;line-height:1;text-align:center;width:100%}
  .wordmark--front{font-size:88px;top:207px}
  .wordmark--back{font-size:54px;top:46px}
  .dots{display:flex;gap:5px}
  .dot{width:11px;height:11px;border-radius:50%}
  .tagline{font-weight:400;font-size:14px;letter-spacing:.1em;color:var(--ink);white-space:nowrap}
  .tagline--vertical{transform:rotate(-90deg);transform-origin:left top}
  .intro{left:66px;width:240px;color:var(--copy);font-size:7.5px;line-height:1.3}
  .intro p{margin-bottom:18px}
  .rule{left:66px;top:276px;width:240px;height:1.5px;background:var(--copy)}
  .lang{left:45px;width:282px;display:flex;align-items:center;gap:8px}
  .flag{flex:0 0 11px;height:11px;border-radius:50%}
  .lang p{color:var(--copy);font-size:6.8px;line-height:1.35;text-align:justify}
  .certs{display:flex;align-items:center;gap:8px}
  .cert{background:var(--ink)}
</style>
</head>
<body>
<div class="canvas">

  <!-- Front face -->
  <div class="abs tab" style="left:268px;top:150px;width:58px;height:55px"></div>
  <div class="abs tray tray--front" style="left:117px;top:205px;width:362px;height:131px">
    <div class="case-photo" role="img" aria-label="White phone case visible inside the tray"></div>
  </div>
  <div class="abs sleeve" style="left:112px;top:336px;width:372px;height:491px">
    <div class="abs wordmark wordmark--front">VAXEL</div>
  </div>
  <div class="abs sleeve-foot" style="left:112px;top:827px;width:372px;height:225px">
    <div class="abs dots" style="left:152px;top:148px">
      <span class="dot" style="background:#3a3a3a"></span>
      <span class="dot" style="background:#4d4d4d"></span>
      <span class="dot" style="background:#666"></span>
      <span class="dot" style="background:#7f7f7f"></span>
      <span class="dot" style="background:#9a9a9a"></span>
    </div>
    <div class="abs tagline" style="left:0;width:372px;text-align:center;top:175px">PREMIUM PHONE CASES</div>
  </div>

  <!-- Side face -->
  <div class="abs tab tab--thin" style="left:593px;top:150px;width:9px;height:55px"></div>
  <div class="abs tray" style="left:551px;top:205px;width:93px;height:131px"></div>
  <div class="abs sleeve" style="left:546px;top:336px;width:103px;height:491px"></div>
  <div class="abs sleeve-foot" style="left:546px;top:827px;width:103px;height:225px">
    <div class="abs" style="left:36px;top:55px;display:flex;flex-direction:column;gap:6px">
      <span class="dot" style="background:#a3a3a3"></span>
      <span class="dot" style="background:#8a8a8a"></span>
      <span class="dot" style="background:#6e6e6e"></span>
      <span class="dot" style="background:#4f4f4f"></span>
      <span class="dot" style="background:#333"></span>
    </div>
    <div class="abs tagline tagline--vertical" style="left:53px;top:192px">PREMIUM PHONE CASES</div>
  </div>

  <!-- Back face -->
  <div class="abs tab" style="left:873px;top:150px;width:58px;height:55px"></div>
  <div class="abs tray" style="left:722px;top:205px;width:362px;height:131px"></div>
  <div class="abs sleeve" style="left:716px;top:336px;width:373px;height:491px">
    <div class="abs wordmark wordmark--back">VAXEL</div>
    <div class="abs intro" style="top:156px">
      <p>Lorem Ipsum is simply dummy text of the printing and typesetting industry. Lorem Ipsum has been the industry's standard dummy</p>
      <p>text ever since the 1500s, when an unknown printer took a galley of type and scrambled it to make a type specimen book. It has survived not only five centuries, but also the leap into electronic</p>
      <p>typesetting, remaining essentially unchanged. It was popularised in the 1960s with</p>
    </div>
    <div class="abs rule"></div>
    <div class="abs lang" style="top:302px">
      <span class="flag" style="background:#2b3f8f"></span>
      <p>Lorem Ipsum is simply dummy text of the printing and typesetting industry. Lorem Ipsum has been the industry's standard dummy text ever since the 1500s, when an unknown printer took a galley of type and scrambled it to make a type specimen book. It has survived not only five centuries, but also the leap into electronic typesetting, remaining essentially unchanged. It was popularised in the 1960s with the release of Typeline sheets containing Lorem Ipsum passages.</p>
    </div>
    <div class="abs lang" style="top:366px">
      <span class="flag" style="background:linear-gradient(90deg,#2b3f8f 33%,#fff 33% 66%,#d02b2b 66%)"></span>
      <p>Lorem Ipsum est simplement un texte factice de l'industrie de l'impression et de la composition. Lorem Ipsum est le texte factice standard de l'industrie depuis les années 1500, quand un imprimeur inconnu a pris une galère de type et l'a brouillé pour en faire un cahier de caractères. Il a survécu non seulement à cinq siècles, mais aussi au saut dans la composition électronique, demeurant essentiellement inchangé.</p>
    </div>
    <div class="abs lang" style="top:428px">
      <span class="flag" style="background:linear-gradient(180deg,#111 33%,#d02b2b 33% 66%,#f0c020 66%)"></span>
      <p>Lorem Ipsum ist einfach Dummy-Text der Druck- und Satzindustrie. Lorem Ipsum ist seit den 1500er Jahren der Standard-Dummy-Text der Branche, als ein unbekannter Drucker eine Galeere vom Typ nahm und daraus ein Musterheft machte. Es hat nicht nur fünf Jahrhunderte überlebt, sondern auch den Sprung in den elektronischen Satz, der im Wesentlichen unverändert blieb.</p>
    </div>
  </div>
  <div class="abs sleeve-foot" style="left:716px;top:827px;width:373px;height:225px">
    <div class="abs certs" style="left:110px;top:180px">
      <span class="cert" style="width:24px;height:16px;border-radius:3px"></span>
      <span class="cert" style="width:16px;height:16px;border-radius:50%"></span>
      <span class="cert" style="width:40px;height:14px;border-radius:3px"></span>
      <span class="cert" style="width:14px;height:14px;border-radius:50%"></span>
      <span class="cert" style="width:14px;height:20px;border-radius:2px"></span>
    </div>
  </div>

</div>
</body>
</html>
```